Need 8.5" x 11" as well as large 11"x17" Posters for our upcoming event

Please include LOGOs in poster
Main logo is Harborview Teen Circle of PL

All high school age faith groups are invited to come and join with 150 to 175 other high school students from various faith traditions to participate in the Harborview Teen Circle of Pine Lakes‘s Annual Kindred Voices Gathering. More than ever, our county and world need young leaders who are willing to learn from each other and build stronger communities!

KINDRED GATHERING
The purpose of this Interfaith Youth Forum is to bring together young people from diverse ethnic, cultural, and religious backgrounds, and to engage them in dialogue. True dialogue is a conversation on a common subject between two or more persons of differing points of view and/or backgrounds. We feel that this commitment to dialogue will affect relationships in a constructive way in our places of worship and in our community.
The forum itself involves having eight religiously diverse high school-age students, one adult, and youth leader around each table to discuss common questions. Our youth leaders act as facilitators, but it is stressed that it is the students we want to hear from.
RSVP for our KINDRED GATHERING before February 18th, 2018
FORUM QUESTIONS Available online at http://htcpl-example.org/home/kindred-fair/

Target Market(s)

Houses of worship, community leaders, High School Students

Industry/Entity Type

Non-Profit

Font styles to use
Serif

Colors
cfdeed
0255a3
f78f20
f37122
f68d4d
faa54b
ffcf3e
ffc214
34a6d7

Requirements
Must have
• Harborview Teen Circle of Pine Lakes's 14th Annual Kindred Gathering & Fair
• TEENS EXPRESSING THEIR FAITH THROUGH ART, MUSIC, AND DIALOGUE
• THIS YEAR'S THEME: “Who Are You?”
• Sunday, March 11th, 2018 11:00am-5:00pm
• Congregation Ner Adamah
• 4187 W Larkmont Rd. Santa Ana, CA 92705
• Email: htcplorg@mailbox-example.com
• Website: HTCPL-example.org
• Facebook: Harborview Teen Circle of Pine Lakes
Nice to have
• Descriptions provided in word doc
Should not have
• -

```html
<!DOCTYPE html>
<html lang="en">
<head>
<meta charset="utf-8">
<title>Harborview Teen Circle of Pine Lakes — 14th Annual Kindred Gathering &amp; Fair</title>
<link rel="stylesheet" href="https://fonts.googleapis.com/css2?family=Arvo:ital,wght@0,400;0,700;1,400;1,700&family=Cabin:wght@400;600;700&family=Yellowtail&display=swap">
<style>
  :root {
    --sky-top: #9cc3e6;
    --sky-mid: #cfdeed;
    --sky-low: #eef4fa;
    --navy: #0255a3;
    --cyan: #34a6d7;
    --orange: #f78f20;
    --orange-deep: #f37122;
    --orange-light: #faa54b;
    --gold: #ffc214;
    --green: #2a8a3a;
    --ink: #1a1a1a;
    --white: #ffffff;
    --grey-text: #333333;
  }
  * { margin: 0; padding: 0; box-sizing: border-box; }
  html, body { width: 845px; height: 1200px; overflow: hidden; background: var(--white); }
  body { font-family: "Cabin", sans-serif; color: var(--ink); }

  .poster { position: relative; width: 845px; height: 1200px; overflow: hidden; }

  /* Header */
  .masthead {
    position: absolute; left: 0; top: 0; width: 845px; height: 230px;
    background: linear-gradient(180deg, var(--sky-top) 0%, var(--sky-mid) 45%, var(--sky-low) 100%);
  }
  .seal {
    position: absolute; left: 74px; top: 44px; width: 138px; height: 138px;
    border-radius: 50%; background: var(--white); border: 2px solid var(--ink);
    display: flex; align-items: center; justify-content: center; text-align: center;
    font-family: "Arvo", serif; font-weight: 700; font-size: 14px; line-height: 1.2; color: var(--ink);
    padding: 16px;
  }
  .org-line {
    position: absolute; left: 285px; top: 62px;
    font-family: "Arvo", serif; font-weight: 700; font-style: italic; font-size: 15px;
    color: var(--ink); text-transform: uppercase; white-space: nowrap;
  }
  .edition {
    position: absolute; left: 272px; top: 84px;
    font-family: "Arvo", serif; font-weight: 700; font-style: italic; font-size: 92px;
    line-height: 1; color: var(--orange); letter-spacing: -4px;
  }
  .edition sup { font-family: "Yellowtail", cursive; font-style: normal; font-weight: 400; font-size: 32px; letter-spacing: 0; vertical-align: 30px; margin-left: 4px; }
  .event-title {
    position: absolute; left: 428px; top: 86px;
    font-family: "Yellowtail", cursive; font-weight: 400; font-size: 46px; line-height: 50px; color: var(--orange);
    white-space: nowrap;
  }

  /* Tagline band */
  .bands { position: absolute; left: 0; top: 214px; width: 845px; height: 98px; }
  .tagline {
    position: absolute; left: 42px; top: 234px; color: var(--white);
    font-family: "Arvo", serif; font-style: italic; text-transform: uppercase; white-space: nowrap;
  }
  .tagline small { display: block; font-size: 15px; font-weight: 400; }
  .tagline strong { display: block; font-size: 25px; font-weight: 700; line-height: 1.1; }
  .theme {
    position: absolute; left: 505px; top: 248px; width: 340px; text-align: center; color: var(--white);
    font-family: "Arvo", serif; text-transform: uppercase; white-space: nowrap;
  }
  .theme small { display: block; font-size: 14px; }
  .theme strong { display: block; font-size: 27px; font-style: italic; font-weight: 700; line-height: 1.1; }

  /* Photo collage */
  .collage { position: absolute; left: 0; top: 296px; width: 845px; height: 324px; }
  .intro {
    position: absolute; left: 262px; top: 545px; width: 520px; text-align: center;
    font-size: 11px; line-height: 14.5px; color: var(--grey-text);
  }

  /* Details */
  .details { position: absolute; left: 0; top: 624px; width: 845px; height: 346px; background: var(--navy); color: var(--white); }
  .when-where {
    position: absolute; left: 0; top: 60px; width: 234px; height: 208px;
    background: var(--cyan); padding: 38px 0 0 48px; font-family: "Arvo", serif;
  }
  .when-where .day { font-size: 33px; color: var(--gold); line-height: 1; }
  .when-where .date { font-size: 16px; font-weight: 700; margin-top: 4px; }
  .when-where .time { font-size: 12px; font-weight: 700; }
  .when-where hr { border: 0; border-top: 1px solid var(--white); width: 154px; margin: 13px 0 9px; }
  .when-where .venue { font-size: 10.5px; font-weight: 700; white-space: nowrap; }
  .when-where .address { font-size: 9.5px; line-height: 12px; margin-top: 3px; }

  .info-col { position: absolute; top: 31px; font-size: 9px; line-height: 12.5px; }
  .info-col.gathering { left: 271px; width: 250px; }
  .info-col.fair { left: 553px; width: 268px; }
  .info-col h2 { font-family: "Arvo", serif; font-weight: 700; font-size: 19px; color: var(--gold); line-height: 1; margin-bottom: 7px; white-space: nowrap; }
  .info-col p { margin-bottom: 11px; }
  .info-col h2.second { margin-top: 20px; }
  .info-col b { font-weight: 700; }

  /* Bottom photo strip */
  .strip { position: absolute; left: 0; top: 974px; width: 845px; height: 133px; display: flex; gap: 7px; }
  .strip .photo { flex: 1; height: 133px; }
  .photo-marbling { background: linear-gradient(135deg, #6b4a3a, #a36d55 50%, #5a3d35); }
  .photo-drums { background: linear-gradient(180deg, #c9b3a4, #8f6c5c 60%, #5b3d33); }
  .photo-group { background: linear-gradient(180deg, #d8cfc8, #8aa7cf 55%, #ede9e6); }

  /* Footer */
  .footer { position: absolute; left: 0; top: 1107px; width: 845px; height: 93px; font-size: 12px; color: var(--grey-text); }
  .contact { position: absolute; display: flex; align-items: center; gap: 6px; white-space: nowrap; }
  .contact.email { left: 52px; top: 26px; }
  .contact.web { left: 275px; top: 26px; }
  .contact.social { left: 52px; top: 51px; }
  .marker-square { width: 10px; height: 10px; background: var(--navy); }
  .partner { position: absolute; display: flex; align-items: center; gap: 6px; font-family: "Arvo", serif; white-space: nowrap; }
  .partner.allies { left: 512px; top: 32px; font-size: 13px; color: var(--navy); }
  .partner.allies .ring { width: 22px; height: 22px; border-radius: 50%; border: 2px solid var(--navy); }
  .partner.congregation { left: 672px; top: 28px; font-size: 10.5px; color: var(--orange-deep); }
  .partner.congregation .block { width: 10px; height: 36px; background: var(--green); }
</style>
</head>
<body>
<main class="poster">

  <header class="masthead">
    <div class="seal">Harborview Teen Circle of PL</div>
    <p class="org-line">Harborview Teen Circle of Pine Lakes's</p>
    <p class="edition">14<sup>Th</sup></p>
    <h1 class="event-title">Annual Kindred<br>Gathering &amp; Fair</h1>
  </header>

  <svg class="bands" width="845" height="98" viewBox="0 0 845 98" aria-hidden="true">
    <polygon points="0,0 522,0 458,82 0,82" fill="var(--orange-light)"/>
    <polygon points="515,16 845,16 845,97 455,97" fill="var(--orange)"/>
  </svg>
  <p class="tagline"><small>Teens expressing their faith through</small><strong>Art, Music, and Dialogue</strong></p>
  <p class="theme"><small>This year's theme:</small><strong>“Who Are You?”</strong></p>

  <svg class="collage" width="845" height="324" viewBox="0 0 845 324">
    <g role="img" aria-label="Photo: large group of teens posing together on a stage with red curtains">
      <polygon points="0,0 447,0 330,159 0,159" fill="#8a3a3a"/>
    </g>
    <g role="img" aria-label="Photo: teens performing a dance on a wooden stage">
      <polygon points="0,164 318,164 202,324 0,324" fill="#6a3e48"/>
    </g>
    <g role="img" aria-label="Photo: audience seated in a temple hall">
      <polygon points="455,0 662,0 500,235 290,235" fill="#b9a189"/>
    </g>
    <g role="img" aria-label="Photo: teens playing keyboard and sitar">
      <polygon points="676,15 845,15 845,113 604,113" fill="#a9a6a4"/>
    </g>
    <g role="img" aria-label="Photo: table with banners of faith symbols and candles">
      <polygon points="600,117 770,117 700,235 520,235" fill="#b84a45"/>
    </g>
    <g role="img" aria-label="Photo: young man playing a drum">
      <polygon points="780,117 845,117 845,235 712,235" fill="#8f6c5a"/>
    </g>
  </svg>
  <p class="intro">All high school age faith groups are invited to come and join with 150 to 175 other high school students from various faith traditions to participate in the Harborview Teen Circle of Pine Lakes‘s Annual Kindred Voices Gathering. More than ever, our county and world need young leaders who are willing to learn from each other and build stronger communities!</p>

  <section class="details">
    <div class="when-where">
      <p class="day">SUNDAY</p>
      <p class="date">March 11th, 2018</p>
      <p class="time">11:00am-5:00pm</p>
      <hr>
      <p class="venue">CONGREGATION NER ADAMAH</p>
      <p class="address">4187 W Larkmont Rd.<br>Pine Lakes, CA 94512</p>
    </div>

    <div class="info-col gathering">
      <h2>KINDRED GATHERING</h2>
      <p>The purpose of this Interfaith Youth Forum is to bring together young people from diverse ethnic, cultural, and religious backgrounds, and to engage them in dialogue. True dialogue is a conversation on a common subject between two or more persons of differing points of view and/or backgrounds. We feel that this commitment to dialogue will affect relationships in a constructive way in our places of worship and in our community.</p>
      <p>The forum itself involves having eight religiously diverse high school-age students, one adult, and youth leader around each table to discuss common questions. Our youth leaders act as facilitators, but it is stressed that it is the students we want to hear from.</p>
      <p>RSVP for our KINDRED GATHERING before<br><b>February 18th, 2018</b></p>
      <p>FORUM QUESTIONS Available online at<br><b>http://htcpl-example.org/home/kindred-fair/</b></p>
    </div>

    <div class="info-col fair">
      <h2>FAITH FESTIVAL</h2>
      <p>The forum will include our Faith Festival portion of the program which families of the participants are welcomed to join. The Festival will include musical performances of all types from diverse religious communities. The differing performing arts include but are not limited to singing, dancing, instrumental music, storytelling, etc.</p>
      <p>To Participate in our Faith Festival (Music, Song, Dance), RSVP by <b>February 11th, 2018</b></p>
      <h2 class="second">ART GALLERY</h2>
      <p>This event will include and Art Gallery display of students' work, highlighting their expressions of faith, and artwork promoting learning, understanding, leadership, and service. Art includes any painting, illustration, sculpture, photography or other visual art.</p>
      <p>Art Work for our Art Galley must be submitted by:<br><b>March 3rd, 2018</b></p>
    </div>
  </section>

  <div class="strip">
    <div class="photo photo-marbling" role="img" aria-label="Photo: hand creating a marbled paint artwork"></div>
    <div class="photo photo-drums" role="img" aria-label="Photo: hall of students at round tables with drums in front"></div>
    <div class="photo photo-group" role="img" aria-label="Photo: group of smiling teen volunteers in matching shirts"></div>
  </div>

  <footer class="footer">
    <p class="contact email">
      <svg width="12" height="9" viewBox="0 0 12 9" aria-hidden="true"><rect width="12" height="9" fill="var(--orange)"/><polyline points="0,0 6,5 12,0" fill="none" stroke="var(--white)" stroke-width="1"/></svg>
      htcplorg@mailbox-example.com
    </p>
    <p class="contact web">
      <svg width="11" height="11" viewBox="0 0 11 11" aria-hidden="true"><circle cx="5.5" cy="5.5" r="4.8" fill="none" stroke="var(--orange)" stroke-width="1.3"/><line x1="0.7" y1="5.5" x2="10.3" y2="5.5" stroke="var(--orange)"/></svg>
      HTCPL-example.org
    </p>
    <p class="contact social"><span class="marker-square"></span>Harborview Teen Circle of Pine Lakes</p>

    <div class="partner allies"><span>Brightpath Allies</span><span class="ring"></span></div>
    <div class="partner congregation"><span class="block"></span><span>Congregation Ner Adamah</span></div>
  </footer>

</main>
</body>
</html>
```